Vintrell Power Point Presentation

We need our presentation designed. Our current presentation is inconsistent, too text heavy, and complicated. We want this to be clean, sleek, and impressive as our references attached are.

Our colors are blue, black, and white.
Our font is roboto.

```html
<!DOCTYPE html>
<html lang="en">
<head>
<meta charset="utf-8">
<title>Vintrell Media Kit</title>
<link href="https://fonts.googleapis.com/css2?family=Roboto:wght@300;400;500;700&display=swap" rel="stylesheet">
<style>
:root{
  --blue:#1a8cff;
  --blue-deep:#0a6fe0;
  --ink:#23262b;
  --dark:#2b2e33;
  --white:#ffffff;
  --paper:#dedfe1;
  --rule:#eceef1;
  --muted:#6b7280;
}
*{box-sizing:border-box;margin:0;padding:0}
html,body{width:1200px;height:2726px;overflow:hidden}
body{background:var(--paper);font-family:'Roboto',sans-serif;color:var(--ink);position:relative}
.slide{position:absolute;width:540px;height:303px;overflow:hidden;background:var(--white)}
.slide--hero{left:235px;top:88px;transform:scale(1.352);transform-origin:0 0}
.brand{display:flex;align-items:center;gap:5px;font-weight:500;color:var(--white)}
.brand__mark{width:18px;height:18px;background:var(--white);border-radius:3px}
.brand--blue{color:var(--blue)}
.brand--blue .brand__mark{background:var(--blue)}
/* cover */
.cover{background:var(--blue)}
.cover__brand{position:absolute;left:40px;top:50px;font-size:20px}
.cover__title{position:absolute;left:40px;top:112px;color:var(--white);font-size:23px;font-weight:700;line-height:1.13}
.cover__date{position:absolute;left:40px;top:176px;color:var(--white);font-size:6px}
.cover__btn{position:absolute;left:40px;top:227px;width:100px;height:15px;border-radius:3px;background:#5eb0ff;color:var(--white);font-size:6px;font-weight:500;text-align:center;line-height:15px;box-shadow:0 2px 0 rgba(0,0,0,.15)}
.cover__foot{position:absolute;left:0;bottom:0;width:100%;height:18px;background:var(--ink);color:var(--white);font-size:5px;text-align:center;line-height:18px}
.cover__foot span{color:var(--blue)}
.photo{position:absolute;border:3px solid var(--white)}
.photo--round{border:4px solid var(--white);border-radius:12px;box-shadow:0 0 0 3px var(--blue-deep)}
.tone-a{background:linear-gradient(135deg,#5b4a3c,#c9b9a2)}
.tone-b{background:linear-gradient(135deg,#2e3a4a,#8fa3b8)}
.tone-c{background:linear-gradient(135deg,#c7c9cc,#3d6fa8)}
.tone-d{background:linear-gradient(135deg,#6a3d1e,#e0a75a)}
.tone-e{background:linear-gradient(135deg,#b52a26,#e9e6e0)}
.tone-f{background:linear-gradient(135deg,#3a5a2a,#f0a040)}
/* content slide chrome */
.head{position:absolute;left:26px;top:26px;display:flex;align-items:center;gap:8px}
.head__mark{width:16px;height:16px;background:var(--blue);border-radius:3px}
.head__title{font-size:19px;font-weight:500;color:var(--ink)}
.sub{position:absolute;left:60px;top:52px;font-size:11.5px;font-weight:300;color:var(--blue);line-height:1.1;width:460px}
.foot{position:absolute;left:16px;bottom:18px;right:16px;height:14px;display:flex;align-items:center;gap:6px}
.foot .brand{font-size:13px}
.foot .brand__mark{width:14px;height:14px}
.foot__rule{flex:1;height:10px;background:var(--rule)}
.foot__num{width:17px;height:11px;background:var(--blue);color:var(--white);font-size:6px;text-align:center;line-height:11px;border-radius:2px}
/* why indoor */
.why__lead{position:absolute;left:0;top:0;width:270px;height:100%;text-align:center}
.why__mark{width:22px;height:22px;background:var(--blue);border-radius:4px;margin:82px auto 10px}
.why__title{font-size:21px;font-weight:500}
.why__text{font-size:10px;font-weight:300;color:var(--blue);width:200px;margin:14px auto 0;line-height:1.15}
.why__col{position:absolute;top:0;height:100%;width:135px;text-align:center;color:var(--white)}
.why__col--blue{left:270px;background:var(--blue)}
.why__col--dark{left:405px;background:var(--dark)}
.why__col h4{font-size:10.5px;font-weight:500;margin-top:22px}
.why__item{margin-top:12px}
.icon{width:24px;height:24px;border-radius:50%;background:var(--ink);margin:0 auto;display:flex;align-items:center;justify-content:center}
.icon--light{background:var(--white)}
.why__item p{font-size:5.3px;line-height:1.1;margin:5px 8px 0}
.why__works{font-size:10px;font-weight:500;margin:20px 0 0}
/* statement */
.statement{background:linear-gradient(120deg,#3b8fe8,#1a6fd8 60%,#2a86ee)}
.statement__text{position:absolute;left:50px;top:80px;width:440px;text-align:center;color:var(--white)}
.statement__text .brand{justify-content:center;font-size:20px;margin-bottom:14px}
.statement__text p{font-size:16px;font-weight:300;line-height:1.15}
/* advertisers */
.band{position:absolute;left:0;top:103px;width:100%;height:132px;background:var(--blue);display:grid;grid-template-columns:repeat(8,55px);grid-auto-rows:45px;gap:8px 9px;padding:14px 20px}
.tile{background:var(--white);border-radius:6px;display:flex;align-items:center;justify-content:center;font-size:7px;font-weight:500;color:var(--ink);text-align:center;line-height:1.05;padding:2px}
/* takeaways */
.take__intro{position:absolute;left:38px;top:92px;font-size:12px;color:var(--blue)}
.take__list{position:absolute;left:38px;top:118px;width:230px;list-style:none}
.take__list li{font-size:7.3px;line-height:1.1;margin-bottom:8px;padding-left:20px;position:relative;color:#444}
.take__list li::before{content:"✓";position:absolute;left:0;color:var(--blue);font-size:7px}
.take__card{position:absolute;left:294px;top:42px;width:220px;height:190px;background:var(--blue);border-radius:26px;transform:rotate(-2deg);color:var(--white);font-weight:500;font-size:15px;display:flex;align-items:center;justify-content:center;text-align:center;line-height:1.5}
/* formats table */
.spec{position:absolute;left:26px;top:95px;width:488px;border-collapse:collapse;font-size:5.6px}
.spec th{background:var(--blue-deep);color:var(--white);text-align:left;padding:6px 3px;font-size:8.5px;font-weight:500;border-right:1px solid var(--white)}
.spec td{padding:7px 3px;border:1px solid #e2e4e8;color:#333;width:33%}
.spec td::before{content:"✓ ";color:var(--blue)}
.spec td:empty::before{content:""}
/* network */
.net__panel{position:absolute;left:24px;top:100px;width:492px;height:152px;border:1px solid #e3e5e8;background:#fafbfc}
.map{position:absolute;background:radial-gradient(ellipse at 55% 55%,#f4c9a8 0%,#e9ebee 55%,#fafbfc 80%)}
.net__label{position:absolute;font-size:11px;color:var(--ink)}
.net__label b{color:var(--blue);font-weight:500}
.stat{position:absolute;width:54px;height:46px;background:var(--blue);border-radius:6px;color:var(--white);text-align:center;padding-top:7px}
.stat b{display:block;font-size:12.5px;font-weight:500}
.stat span{display:block;font-size:4.8px;margin-top:3px;line-height:1.05}
.note{position:absolute;font-size:4.8px;color:#555;text-align:right}
.net2__box{position:absolute;top:100px;height:150px;border:1px solid #e3e5e8}
/* how to buy */
.buy__row{position:absolute;left:24px;width:492px;height:46px;border:1px solid #e6e8eb;display:flex;align-items:center}
.buy__label{width:112px;padding-left:12px;font-size:12px;font-weight:300;color:var(--ink);line-height:1.05}
.buy__label b{color:var(--blue);font-weight:500}
.buy__cell{flex:1;height:100%;border-left:1px solid #e6e8eb;display:flex;align-items:center;gap:8px;padding-left:10px;font-size:7px;color:#444;line-height:1.05}
.buy__cell svg{flex:none}
.partners{flex:1;height:100%;display:grid;grid-template-columns:repeat(5,1fr);align-items:center;font-size:7px;font-weight:500;color:var(--ink);text-align:center;border-left:1px solid #e6e8eb}
/* thanks */
.thanks{left:330px;top:2375px;background:linear-gradient(120deg,#2f86e6,#1a6fd8 60%,#2f8cf0)}
.thanks__brand{position:absolute;left:58px;top:130px;font-size:20px}
.thanks__title{position:absolute;left:58px;top:172px;color:var(--white);font-size:25px;font-weight:700}
.thanks__sub{position:absolute;left:58px;top:206px;color:var(--white);font-size:10px;font-weight:300}
</style>
</head>
<body>

<!-- Hero cover -->
<section class="slide cover slide--hero">
  <div class="brand cover__brand"><span class="brand__mark"></span>Vintrell</div>
  <h1 class="cover__title">Indoor DOOH<br>Audiences at Scale</h1>
  <p class="cover__date">Wednesday, December 1, 2021</p>
  <div class="cover__btn">BUY ON VINTRELL</div>
  <div class="photo tone-a" style="left:286px;top:6px;width:83px;height:82px" role="img" aria-label="Pharmacy aisle with ceiling screen"></div>
  <div class="photo tone-b" style="left:375px;top:6px;width:160px;height:82px" role="img" aria-label="Venue interior with wall screens"></div>
  <div class="photo tone-c" style="left:286px;top:94px;width:160px;height:82px" role="img" aria-label="Person passing a standing digital kiosk"></div>
  <div class="photo tone-d" style="left:452px;top:94px;width:83px;height:82px" role="img" aria-label="Restaurant bar with screens"></div>
  <div class="photo tone-e" style="left:286px;top:182px;width:83px;height:100px" role="img" aria-label="Shopper watching a store screen"></div>
  <div class="photo tone-f" style="left:375px;top:182px;width:160px;height:100px" role="img" aria-label="Grocery store with coupon screens"></div>
  <div class="cover__foot">Info@<span>Vintrell</span>.com | <span>MEDIA KIT</span> 2021</div>
</section>

<!-- Cover variant A -->
<section class="slide cover" style="left:51px;top:765px">
  <div class="brand cover__brand"><span class="brand__mark"></span>Vintrell</div>
  <h2 class="cover__title">Indoor DOOH<br>Audiences at Scale</h2>
  <p class="cover__date">Wednesday, December 1, 2021</p>
  <div class="cover__btn">BUY ON VINTRELL</div>
  <div class="photo tone-a" style="left:286px;top:6px;width:83px;height:82px" role="img" aria-label="Pharmacy aisle with ceiling screen"></div>
  <div class="photo tone-b" style="left:375px;top:6px;width:160px;height:82px" role="img" aria-label="Venue interior with wall screens"></div>
  <div class="photo tone-c" style="left:286px;top:94px;width:160px;height:82px" role="img" aria-label="Person passing a standing digital kiosk"></div>
  <div class="photo tone-d" style="left:452px;top:94px;width:83px;height:82px" role="img" aria-label="Restaurant bar with screens"></div>
  <div class="photo tone-e" style="left:286px;top:182px;width:83px;height:100px" role="img" aria-label="Shopper watching a store screen"></div>
  <div class="photo tone-f" style="left:375px;top:182px;width:160px;height:100px" role="img" aria-label="Grocery store with coupon screens"></div>
  <div class="cover__foot">Info@<span>Vintrell</span>.com | <span>MEDIA KIT</span> 2021</div>
</section>

<!-- Cover variant B -->
<section class="slide cover" style="left:609px;top:765px">
  <div class="brand cover__brand"><span class="brand__mark"></span>Vintrell</div>
  <h2 class="cover__title">Indoor DOOH<br>Audiences at Scale</h2>
  <p class="cover__date">Wednesday, December 1, 2021</p>
  <div class="cover__btn">BUY ON VINTRELL</div>
  <div class="photo photo--round tone-e" style="left:288px;top:18px;width:82px;height:68px" role="img" aria-label="Shopper watching a store screen"></div>
  <div class="photo photo--round tone-c" style="left:288px;top:108px;width:82px;height:68px" role="img" aria-label="Store entrance screen"></div>
  <div class="photo photo--round tone-c" style="left:288px;top:198px;width:82px;height:68px" role="img" aria-label="Person passing a standing digital kiosk"></div>
  <div class="photo photo--round tone-d" style="left:390px;top:18px;width:138px;height:115px" role="img" aria-label="Restaurant bar with screens"></div>
  <div class="photo photo--round tone-f" style="left:390px;top:150px;width:138px;height:115px" role="img" aria-label="Grocery store with coupon screens"></div>
  <div class="cover__foot">Info@<span>Vintrell</span>.com | <span>MEDIA KIT</span> 2021</div>
</section>

<!-- Why go indoor -->
<section class="slide why" style="left:51px;top:1087px">
  <div class="why__lead">
    <div class="why__mark"></div>
    <h2 class="why__title">Why Go Indoor</h2>
    <p class="why__text">it's not just lockdowns ending - recent uptick has been driven by the unique effectiveness of indoor DOOH ad exposure.</p>
  </div>
  <div class="why__col why__col--blue">
    <h4>It's special...</h4>
    <div class="why__item"><div class="icon"><svg width="12" height="8" viewBox="0 0 12 8"><ellipse cx="6" cy="4" rx="5.5" ry="3.5" fill="#fff"/><circle cx="6" cy="4" r="1.8" fill="#23262b"/></svg></div><p>Dwell time measured in minutes, not seconds</p></div>
    <div class="why__item"><div class="icon"><svg width="10" height="12" viewBox="0 0 10 12"><text x="5" y="10" font-size="11" font-weight="700" fill="#fff" text-anchor="middle" font-family="Roboto,sans-serif">$</text></svg></div><p>Brand-safe</p></div>
    <div class="why__item"><div class="icon"><svg width="12" height="12" viewBox="0 0 12 12"><circle cx="6" cy="4" r="2.5" fill="#fff"/><path d="M1.5 11a4.5 4 0 0 1 9 0z" fill="#fff"/></svg></div><p>100% viewability by humans, not bots</p></div>
    <div class="why__item"><div class="icon"><svg width="12" height="12" viewBox="0 0 12 12"><rect x="1" y="2" width="10" height="8" rx="2" fill="#fff"/><circle cx="6" cy="6" r="2" fill="#23262b"/></svg></div><p>Not<br>Skippable</p></div>
  </div>
  <div class="why__col why__col--dark">
    <h4>It's powerful...</h4>
    <div class="why__item"><div class="icon" style="background:var(--blue)"><svg width="12" height="12" viewBox="0 0 12 12"><path d="M2 4h3l4-3v10L5 8H2z" fill="#fff"/></svg></div><p>Engaged impressions, consumer attention, means...</p></div>
    <div class="why__item"><div class="icon" style="background:var(--blue)"><svg width="12" height="12" viewBox="0 0 12 12"><circle cx="6" cy="6" r="4.5" fill="none" stroke="#fff" stroke-width="1.2"/><circle cx="6" cy="6" r="1.6" fill="#fff"/></svg></div><p>...Indoor DOOH 2x more likely to be seen, recalled, than traditional OOH</p></div>
    <p class="why__works">And it works.</p>
    <div class="why__item"><div class="icon" style="background:var(--blue)"><svg width="12" height="12" viewBox="0 0 12 12"><path d="M2 6a4 4 0 0 1 7-2.6M10 6a4 4 0 0 1-7 2.6" fill="none" stroke="#fff" stroke-width="1.4"/></svg></div><p>2x increase in reach if added to Omni-Channel campaigns</p></div>
  </div>
  <div class="foot"><div class="brand brand--blue"><span class="brand__mark"></span>Vintrell</div><div class="foot__rule"></div><div class="foot__num">3</div></div>
</section>

<!-- Statement -->
<section class="slide statement" style="left:609px;top:1087px" role="img" aria-label="Person facing a digital kiosk, tinted blue">
  <div class="statement__text">
    <div class="brand"><span class="brand__mark"></span>Vintrell</div>
    <p>Vintrell offers advertisers easy, affordable access to North America's largest indoor DOOH network, containing diverse audience segments while captivated in indoor environments</p>
  </div>
</section>

<!-- Advertisers -->
<section class="slide" style="left:51px;top:1409px">
  <div class="head"><span class="head__mark"></span><h2 class="head__title">Advertisers</h2></div>
  <p class="sub">Brands that buy on our network.</p>
  <div class="band">
    <div class="tile">Corvan</div><div class="tile">Bunlo</div><div class="tile">Rinkwell</div><div class="tile">Fizzlo</div>
    <div class="tile">Hoagio</div><div class="tile">Starvale</div><div class="tile">Maison Orre</div><div class="tile">Dravo</div>
    <div class="tile">Hemly</div><div class="tile">Candri</div><div class="tile">Tavenne</div><div class="tile">Pixoro</div>
    <div class="tile">Northfizz</div><div class="tile">Tunely</div><div class="tile">Kestrel Bank</div><div class="tile">Dashly</div>
  </div>
  <div class="foot"><div class="brand brand--blue"><span class="brand__mark"></span>Vintrell</div><div class="foot__rule"></div><div class="foot__num">5</div></div>
</section>

<!-- Key takeaways -->
<section class="slide" style="left:609px;top:1409px">
  <div class="head"><span class="head__mark"></span><h2 class="head__title">Key Takeaways</h2></div>
  <p class="take__intro">Vintrell is:</p>
  <ul class="take__list">
    <li>North America's largest and fastest-growing indoor DOOH screen network</li>
    <li>Powerful enough to capture the attention of nationwide audiences at scale, specific enough to provide access to diverse audience segments</li>
    <li>Programmatically-accessible, ensuring cost-efficiency, transparency and real-time optimizations</li>
    <li>Flexible enough to get any DOOH campaign or integration up and running quickly and without issue</li>
  </ul>
  <div class="take__card">The Right Time.<br>The Right Message.<br>The Right Audience.</div>
  <div class="foot"><div class="brand brand--blue"><span class="brand__mark"></span>Vintrell</div><div class="foot__rule"></div><div class="foot__num">6</div></div>
</section>

<!-- Formats -->
<section class="slide" style="left:51px;top:1731px">
  <div class="head"><span class="head__mark"></span><h2 class="head__title">Digital Media Formats</h2></div>
  <p class="sub">Specifications</p>
  <table class="spec">
    <tr><th>Network</th><th>Content Specifications</th><th>Ad Content Play Suggestions</th></tr>
    <tr><td>Indoor, 32 – 73" Screens</td><td>1920 pixels (w) x 1080 pixels (h) 16:9</td><td>15 second</td></tr>
    <tr><td>Full Screen Take Over</td><td>1080 pixels (w) x 1920 pixels (h) 9:16</td><td>30 second</td></tr>
    <tr><td>Sold programmatically</td><td>Static: PNG, RGB, encoded. JPG or H.264</td><td>60 second</td></tr>
    <tr><td>No Blacklisted Advertisers</td><td>Video: .MP$ / encoded .MOV</td><td></td></tr>
    <tr><td>Approval Upon Venue Review</td><td>Will repurpose TV spots, banner ads; transcode ill-fitting static creatives</td><td></td></tr>
  </table>
  <div class="foot"><div class="brand brand--blue"><span class="brand__mark"></span>Vintrell</div><div class="foot__rule"></div><div class="foot__num">7</div></div>
</section>

<!-- Network A -->
<section class="slide" style="left:609px;top:1731px">
  <div class="head"><span class="head__mark"></span><h2 class="head__title">Network</h2></div>
  <p class="sub">Vintrell is your DOOH partner, connecting your partners and advertisers to a nation-wide network of premium, place-based screens.</p>
  <div class="net__panel">
    <div class="map" style="left:150px;top:20px;width:200px;height:130px" role="img" aria-label="Map of North America with venue locations"></div>
    <p class="net__label" style="left:18px;top:8px">Our <b>Nationwide</b> Network</p>
    <p class="net__label" style="right:18px;top:8px">Our <b>Premium</b> Venue Types</p>
    <div class="stat" style="left:14px;top:28px"><b>12B+</b><span>Impressions<br>Annually</span></div>
    <div class="stat" style="left:72px;top:28px"><b>50+</b><span>DMA's</span></div>
    <div class="stat" style="left:14px;top:81px"><b>26,105+</b><span>Venues</span></div>
    <div class="stat" style="left:72px;top:81px"><b>31,594+</b><span>Screens</span></div>
    <div class="stat" style="left:362px;top:28px"><b>2000+</b><span>Medical<br>Screens</span></div>
    <div class="stat" style="left:420px;top:28px"><b>4000+</b><span>Grocery<br>Screens</span></div>
    <div class="stat" style="left:362px;top:81px"><b>12000+</b><span>Retail<br>Screens</span></div>
    <div class="stat" style="left:420px;top:81px"><b>16000</b><span>Restobar<br>Screens</span></div>
    <p class="note" style="right:12px;top:134px">Plus private airports, hockey arenas,<br>records stores, and many more.</p>
  </div>
  <div class="foot"><div class="brand brand--blue"><span class="brand__mark"></span>Vintrell</div><div class="foot__rule"></div><div class="foot__num">8</div></div>
</section>

<!-- Network B -->
<section class="slide" style="left:51px;top:2053px">
  <div class="head"><span class="head__mark"></span><h2 class="head__title">Network</h2></div>
  <p class="sub">Vintrell is your DOOH partner, connecting your partners and advertisers to a nation-wide network of premium, place-based screens.</p>
  <div class="net2__box" style="left:24px;width:240px">
    <p class="net__label" style="left:8px;top:8px">Our <b>Nationwide</b> Network.</p>
    <div class="stat" style="left:6px;top:28px"><b>12B+</b><span>Impressions<br>Annually</span></div>
    <div class="stat" style="left:64px;top:28px"><b>50+</b><span>DMA's</span></div>
    <div class="stat" style="left:122px;top:28px"><b>26,105+</b><span>Venues</span></div>
    <div class="stat" style="left:180px;top:28px"><b>31,594+</b><span>Screens</span></div>
    <div class="map" style="left:6px;top:80px;width:226px;height:66px" role="img" aria-label="Map of North America with venue locations"></div>
  </div>
  <div class="net2__box" style="left:272px;width:244px">
    <p class="net__label" style="left:8px;top:8px">Our <b>Premium</b> Venue Types.</p>
    <div class="stat" style="left:6px;top:28px"><b>12000+</b><span>Retail<br>Screens</span></div>
    <div class="stat" style="left:64px;top:28px"><b>16000</b><span>Restobar<br>Screens</span></div>
    <div class="stat" style="left:122px;top:28px"><b>2000+</b><span>Medical<br>Screens</span></div>
    <div class="stat" style="left:180px;top:28px"><b>4000+</b><span>Grocery<br>Screens</span></div>
    <p class="note" style="left:8px;top:79px;text-align:left">Plus private airports, hockey arenas, records stores, and many more.</p>
    <div class="tone-a" style="position:absolute;left:8px;top:92px;width:72px;height:48px" role="img" aria-label="Pharmacy screen"></div>
    <div class="tone-d" style="position:absolute;left:86px;top:92px;width:72px;height:48px" role="img" aria-label="Restobar screens"></div>
    <div class="tone-c" style="position:absolute;left:164px;top:92px;width:72px;height:48px" role="img" aria-label="Gym screens"></div>
  </div>
  <div class="foot"><div class="brand brand--blue"><span class="brand__mark"></span>Vintrell</div><div class="foot__rule"></div><div class="foot__num">9</div></div>
</section>

<!-- How to buy -->
<section class="slide" style="left:609px;top:2053px">
  <div class="head"><span class="head__mark"></span><h2 class="head__title">How To Buy</h2></div>
  <p class="sub">Vintrell's network and unique audiences are accessible however you buy your media.</p>
  <div class="buy__row" style="top:88px">
    <p class="buy__label"><b>Audiences...</b></p>
    <div class="buy__cell"><svg width="22" height="22" viewBox="0 0 22 22"><circle cx="8" cy="8" r="5" fill="none" stroke="#1a8cff" stroke-width="1.5"/><circle cx="15" cy="14" r="5" fill="none" stroke="#1a8cff" stroke-width="1.5"/></svg>High<br>Net Worth</div>
    <div class="buy__cell"><svg width="22" height="16" viewBox="0 0 22 16"><rect x="1" y="1" width="20" height="14" fill="none" stroke="#1a8cff" stroke-width="1.5"/><line x1="11" y1="1" x2="11" y2="15" stroke="#1a8cff" stroke-width="1.5"/><circle cx="11" cy="8" r="3" fill="none" stroke="#1a8cff" stroke-width="1.5"/></svg>Sports<br>Fans</div>
    <div class="buy__cell"><svg width="22" height="22" viewBox="0 0 22 22"><circle cx="14" cy="7" r="5" fill="none" stroke="#1a8cff" stroke-width="1.5"/><path d="M14 4v3h2" stroke="#1a8cff" stroke-width="1.5" fill="none"/><circle cx="6" cy="10" r="2" fill="#1a8cff"/><path d="M3 21v-6h6v6" stroke="#1a8cff" stroke-width="1.5" fill="none"/></svg>High<br>Dwell Time</div>
  </div>
  <div class="buy__row" style="top:140px">
    <p class="buy__label">... you can buy<br><b>anywhere...</b></p>
    <div class="partners" style="grid-template-rows:1fr 1fr">
      <span>Ovira</span><span>Pathmo</span><span>Adquant</span><span>Telvo Media</span><span>Brightmark</span>
      <span>Lumeq</span><span>BidHarbor</span><span>Combnet</span><span>Beatline</span><span>Tentwise</span>
    </div>
  </div>
  <div class="buy__row" style="top:192px">
    <p class="buy__label">...however<br><b>you'd like.</b></p>
    <div class="buy__cell"><svg width="22" height="22" viewBox="0 0 22 22"><path d="M3 12l7-8 9 9-7 6z" fill="none" stroke="#1a8cff" stroke-width="1.5"/></svg>Direct<br>Buying</div>
    <div class="buy__cell"><svg width="22" height="22" viewBox="0 0 22 22"><circle cx="11" cy="11" r="3" fill="none" stroke="#1a8cff" stroke-width="1.5"/><circle cx="3" cy="3" r="2" fill="#1a8cff"/><circle cx="19" cy="3" r="2" fill="#1a8cff"/><circle cx="3" cy="19" r="2" fill="#1a8cff"/><circle cx="19" cy="19" r="2" fill="#1a8cff"/><path d="M4 4l5 5M18 4l-5 5M4 18l5-5M18 18l-5-5" stroke="#1a8cff" stroke-width="1.2"/></svg>Open<br>RTB</div>
    <div class="buy__cell"><svg width="22" height="22" viewBox="0 0 22 22"><rect x="2" y="3" width="16" height="12" fill="none" stroke="#1a8cff" stroke-width="1.5"/><path d="M10 10v10l3-3 3 4" stroke="#1a8cff" stroke-width="1.5" fill="none"/></svg>Programmatic<br>Guaranteed<br>Or PMP</div>
  </div>
  <div class="foot"><div class="brand brand--blue"><span class="brand__mark"></span>Vintrell</div><div class="foot__rule"></div><div class="foot__num">10</div></div>
</section>

<!-- Thank you -->
<section class="slide thanks" role="img" aria-label="Person facing a digital kiosk, tinted blue">
  <div class="brand thanks__brand"><span class="brand__mark"></span>Vintrell</div>
  <h2 class="thanks__title">Thank You!</h2>
  <p class="thanks__sub">for your Time and Attention ...</p>
  <div class="cover__foot">Info@<span>Vintrell</span>.com | <span>MEDIA KIT</span> 2021</div>
</section>

</body>
</html>
```